Graphic Design 4x 960x360 CAROUSELLA PANELS for Design Project for Velbrook Nutrition

Hi,

I want to update my website sliders to make it look more sports nutrition related and more fitting for my business. You can view my website at www.velbrooknutrition-example.com and I would like 4 sliders for the site. Read my blogs too to learn more about what I do.

I would like to highlight my logo and my tag line within my logo of happy, healthy, and oxygenated. Pictures of me intertwined in sliders ok as well.

Carousella Panels size: 960x360 PLEASE REVIEW THIS SAMPLE VERSION of the slides I like and similar. PLEASE REVIEW FILE #2 THANK You. :)

Additionally, some words I like are GameChanger on a slide.
Recovery and Rebound, and the theme and main meaning of Velbrook (Happiness, Healthy, and Oxygen) all realated to fitness, health, medical nutritional therapy.

Thank you so much and looking forward!

Hi everyone, 

Hope your all doing great. I updated a File #2 slide for you to review on an example of the slides and style I like. Thank you for all your hard work! 

Hi all,

Hope all is well. I wanted to guide you more on a 2 slides. I am interested in a slide that has a beach theme and happy, healthy, and fitness people working out in the background playing volleyball, surfing, and running. Also eating some fruit would be nice. Then another slide with Velbrook Nutrition on  a billboard and the billboard looking with healthy and happy. Maybe symbol on there and more dynamic feelings around that. Thanks again and I extended the date. Hope this update helps. 

Reason: I am still looking for the perfect design. The newest ones are on the right track. I appreciate everyone so much. Lots of health, happiness, and oxygen.

Hello Everyone,

I hope all is well. I am going to extend the project because I am going on a business trip. PLease review some of the updates I did to the main aspect and some attachments I did add as well. 

Reason: Would love to see you shine in your creativity within the business.

Reason: I would love to see other options and the big billboard Of velbrook Nutrition. I have been out of town so I apologize for not making updates. please let me know if your interested and submit some designs. thank you your beautiful!

hello all,

I would love if you could make a slide that states to visit the Velbrook Nutrition Online store. 

To schedule appointments and order the best quality supplements. 
KTP Approved for Athletics

Reason: I would love to extend this so we can move forward. Thank you.

Target Market(s)

Happy, Healthy, Sports, fitness, medical, and sports professionals

Industry/Entity Type

Nutrition

Requirements
Must have
• Theme and Logo of Velbrook Nutrition.

```html
<!DOCTYPE html>
<html lang="en">
<head>
<meta charset="utf-8">
<title>Velbrook Nutrition – Recovery &amp; Rebound</title>
<link rel="stylesheet" href="https://fonts.googleapis.com/css2?family=Arimo:wght@400;700&family=Lexend:wght@300&display=swap">
<style>
  :root {
    --blue-deep: #0b3784;
    --blue-mid: #1f63be;
    --blue-glow: #56a8e6;
    --white: #ffffff;
    --ice: #d6ecfb;
    --divider: rgba(255, 255, 255, 0.75);
    --stripe: rgba(255, 255, 255, 0.12);
  }
  html, body {
    margin: 0;
    padding: 0;
    overflow: hidden;
    background: var(--blue-deep);
  }
  .slide {
    position: relative;
    width: 1200px;
    height: 450px;
    overflow: hidden;
    background:
      radial-gradient(ellipse 620px 360px at 640px 250px, var(--blue-glow) 0%, var(--blue-mid) 45%, var(--blue-deep) 100%);
    font-family: "Arimo", Arial, sans-serif;
    color: var(--white);
  }
  .stripes {
    position: absolute;
    inset: 0;
  }
  .clock-area {
    position: absolute;
    left: 915px;
    top: 140px;
    width: 400px;
    height: 400px;
    border-radius: 50%;
    background: radial-gradient(circle, rgba(214, 236, 251, 0.16) 0%, rgba(214, 236, 251, 0.08) 60%, rgba(214, 236, 251, 0) 72%);
  }
  .brand {
    position: absolute;
    left: 48px;
    top: 78px;
    display: flex;
    align-items: center;
    gap: 14px;
  }
  .brand-dot {
    width: 48px;
    height: 48px;
    border-radius: 50%;
    background: var(--white);
  }
  .brand-name {
    font-weight: 700;
    font-size: 34px;
    color: var(--white);
    white-space: nowrap;
  }
  .divider {
    position: absolute;
    left: 440px;
    top: 28px;
    width: 3px;
    height: 146px;
    background: var(--divider);
  }
  .headline {
    position: absolute;
    left: 474px;
    top: 70px;
    margin: 0;
    font-family: "Lexend", Arial, sans-serif;
    font-weight: 300;
    font-size: 46px;
    letter-spacing: 2px;
    color: var(--ice);
    text-shadow: 0 2px 4px rgba(0, 20, 70, 0.45);
    white-space: nowrap;
  }
  .lead {
    position: absolute;
    left: 78px;
    top: 232px;
    margin: 0;
    width: 860px;
    font-size: 38px;
    line-height: 50px;
    font-weight: 400;
    color: var(--white);
  }
</style>
</head>
<body>
  <div class="slide">
    <svg class="stripes" width="1200" height="450" viewBox="0 0 1200 450" aria-hidden="true">
      <polygon points="0,330 230,0 262,0 0,376" fill="var(--stripe)"/>
      <polygon points="62,450 374,0 410,0 98,450" fill="var(--stripe)"/>
    </svg>

    <div class="clock-area" role="img" aria-label="Faint clock face with tick marks and hands"></div>

    <div class="brand">
      <span class="brand-dot"></span>
      <span class="brand-name">Velbrook Nutrition</span>
    </div>

    <div class="divider"></div>

    <h1 class="headline">RECOVERY &amp; REBOUND</h1>

    <p class="lead">Follow my nutritional recommendations to have a faster recovery after working out and even after injury or surgery.</p>
  </div>
</body>
</html>
```